This Project is listed for : Vexmoor only ... if you are not Vexmoors, please do not submit please

This is the listing for

Torbesca

business cards
very simple, elegant and firm
Black / Red / White

Target Market(s)

Adults
Investors
Clients

Industry/Entity Type

Business

Font styles to use
Decorative
Script

```html
<!DOCTYPE html>
<html lang="en">
<head>
<meta charset="utf-8">
<title>Torbesca — Business Card</title>
<link rel="stylesheet" href="https://fonts.googleapis.com/css2?family=Pinyon+Script&family=EB+Garamond:ital,wght@1,400;1,500&display=swap">
<style>
  :root {
    --ink: #000000;
    --paper: #ffffff;
    --accent: #d7141a;
    --rule-grey: #8a8a8a;
    --script: "Pinyon Script", cursive;
    --serif: "EB Garamond", serif;
  }
  * { margin: 0; padding: 0; box-sizing: border-box; }
  html, body { width: 1050px; height: 1200px; overflow: hidden; background: var(--paper); }
  .sheet { position: relative; width: 1050px; height: 1200px; }

  /* Card front */
  .card-front {
    position: absolute; left: 0; top: 0; width: 1050px; height: 600px;
    background: var(--ink);
  }
  .front-frame { position: absolute; left: 0; top: 0; }
  .front-wordmark {
    position: absolute; left: 0; top: 200px; width: 1050px;
    text-align: center; font-family: var(--script); font-size: 150px;
    line-height: 1; color: var(--paper); font-weight: 400;
  }

  /* Card back */
  .card-back {
    position: absolute; left: 0; top: 600px; width: 1050px; height: 600px;
    background: var(--paper);
  }
  .back-wordmark {
    position: absolute; left: 48px; top: 14px;
    font-family: var(--script); font-size: 64px; line-height: 1;
    color: var(--ink); font-weight: 400;
  }
  .wordmark-rule { position: absolute; left: 48px; top: 76px; }
  .holder-name {
    position: absolute; left: 0; top: 160px; width: 1050px; text-align: center;
    font-family: var(--script); font-size: 100px; line-height: 1;
    color: var(--ink); padding-left: 24px;
  }
  .holder-title {
    position: absolute; left: 0; top: 296px; width: 1050px; text-align: center;
    font-family: var(--script); font-size: 46px; line-height: 1;
    color: var(--accent); padding-left: 18px;
  }
  .divider {
    position: absolute; left: 78px; top: 355px; width: 894px; height: 12px;
    background: var(--rule-grey); opacity: .55;
  }
  .contact {
    position: absolute; font-family: var(--serif); font-style: italic;
    font-size: 38px; line-height: 1; color: var(--ink); white-space: nowrap;
  }
  .contact-email { left: 256px; top: 388px; }
  .contact-fax { left: 648px; top: 388px; }
  .contact-phone { left: 388px; top: 478px; }
</style>
</head>
<body>
<main class="sheet">
  <section class="card-front">
    <svg class="front-frame" width="1050" height="600" role="img" aria-label="Twisted rope border framing the card front">
      <rect x="26" y="26" width="998" height="544" fill="none" stroke="var(--paper)" stroke-width="8" opacity="0.85"/>
    </svg>
    <div class="front-wordmark">Torbesca</div>
  </section>

  <section class="card-back">
    <div class="back-wordmark">Torbesca</div>
    <svg class="wordmark-rule" width="616" height="8" aria-hidden="true">
      <line x1="0" y1="1" x2="616" y2="1" stroke="var(--accent)" stroke-width="1.2"/>
      <line x1="0" y1="6" x2="616" y2="6" stroke="var(--accent)" stroke-width="1.2"/>
    </svg>
    <h1 class="holder-name">Name</h1>
    <p class="holder-title">Title</p>
    <div class="divider" role="img" aria-label="Row of small diamond ornaments as a divider"></div>
    <p class="contact contact-email">Em@il</p>
    <p class="contact contact-fax">Fax Number</p>
    <p class="contact contact-phone">Phone Number</p>
  </section>
</main>
</body>
</html>
```